Medical Waste Company with Logo

Need a business card design that targets office managers in the medical community. This card will be the front line for our sales team to market our services to the community. We would like to have email, phone number, website. Please use the logo attached to create a design that we would be proud of.

Target Market(s)

Medical Clients

Industry/Entity Type

Medical Supply

Contact Information for Business Card

Please use logo attached

Colors

Designer to choose colors to be used in the design.

Requirements
Must have
• Our logo (see attached file)
Nice to have
• Maybe a pop of some sort, raised..?

```html
<!DOCTYPE html>
<html lang="en">
<head>
<meta charset="utf-8">
<title>Northpeak Clinical Disposal – Business Card</title>
<link rel="stylesheet" href="https://fonts.googleapis.com/css2?family=Open+Sans:wght@400;600;700&display=swap">
<style>
  :root {
    --page-bg: #5f5f5f;
    --card-white: #ffffff;
    --brand-blue: #1b65a3;
    --deep-blue: #0d3f7e;
    --mid-blue: #1c63a6;
    --ink-grey: #4a4a4a;
    --soft-grey: #6b6b6b;
  }
  * { box-sizing: border-box; margin: 0; padding: 0; }
  html, body {
    width: 1200px; height: 1200px; overflow: hidden;
    background: var(--page-bg);
    font-family: "Open Sans", Arial, sans-serif;
  }
  .sheet {
    width: 1200px; height: 1200px;
    display: flex; flex-direction: column; align-items: center; justify-content: center;
    gap: 36px;
  }
  .card {
    width: 900px; height: 514px; position: relative; overflow: hidden;
    box-shadow: 0 10px 28px rgba(0,0,0,.35);
  }

  /* Front */
  .card-front { background: var(--card-white); }
  .front-band {
    position: absolute; left: 0; right: 0; bottom: 0; height: 150px;
    background: var(--brand-blue);
    display: flex; align-items: center; justify-content: center;
  }
  .website { color: var(--card-white); font-size: 24px; letter-spacing: .3px; }
  .brand-block {
    position: absolute; left: 70px; top: 120px; width: 360px;
    display: flex; align-items: center; gap: 14px;
  }
  .brand-square { width: 22px; height: 22px; background: var(--brand-blue); flex: none; }
  .brand-name {
    color: var(--brand-blue); font-weight: 700; font-size: 30px; line-height: 1.15;
    text-transform: uppercase; letter-spacing: .5px;
  }
  .divider {
    position: absolute; left: 470px; top: 80px; width: 1.5px; height: 250px;
    background: var(--brand-blue);
  }
  .contact {
    position: absolute; left: 505px; top: 88px; width: 370px; color: var(--ink-grey);
  }
  .person-name { color: var(--brand-blue); font-weight: 700; font-size: 28px; letter-spacing: .5px; }
  .person-role { color: var(--soft-grey); font-size: 19px; margin-bottom: 20px; }
  .contact-row { display: flex; align-items: flex-start; gap: 10px; font-size: 19px; line-height: 1.4; margin-bottom: 4px; }
  .contact-row svg { width: 18px; height: 18px; flex: none; margin-top: 5px; fill: var(--brand-blue); }

  /* Back */
  .card-back {
    background: linear-gradient(135deg, var(--deep-blue) 0%, var(--mid-blue) 55%, #0f4d92 100%);
    display: flex; align-items: center; justify-content: center;
  }
  .back-brand { display: flex; align-items: center; gap: 18px; }
  .back-brand .brand-square { width: 30px; height: 30px; background: var(--card-white); }
  .back-brand .brand-name { color: var(--card-white); font-size: 40px; }
</style>
</head>
<body>
<main class="sheet">
  <section class="card card-front">
    <div class="brand-block">
      <span class="brand-square"></span>
      <span class="brand-name">Northpeak<br>Clinical Disposal</span>
    </div>
    <div class="divider"></div>
    <div class="contact">
      <div class="person-name">JOHN DOE</div>
      <div class="person-role">Doctor</div>
      <div class="contact-row">
        <svg viewBox="0 0 24 24"><path d="M12 2a7 7 0 0 0-7 7c0 5.2 7 13 7 13s7-7.8 7-13a7 7 0 0 0-7-7zm0 9.5A2.5 2.5 0 1 1 12 6.5a2.5 2.5 0 0 1 0 5z"/></svg>
        <span>Dummy city<br>Dummy Country Land</span>
      </div>
      <div class="contact-row">
        <svg viewBox="0 0 24 24"><path d="M6.6 10.8a15 15 0 0 0 6.6 6.6l2.2-2.2a1 1 0 0 1 1-.25 11.4 11.4 0 0 0 3.6.57 1 1 0 0 1 1 1V20a1 1 0 0 1-1 1A17 17 0 0 1 3 4a1 1 0 0 1 1-1h3.5a1 1 0 0 1 1 1c0 1.25.2 2.45.57 3.6a1 1 0 0 1-.25 1z"/></svg>
        <span>1-234-567890</span>
      </div>
      <div class="contact-row">
        <svg viewBox="0 0 24 24"><path d="M3 5h18v14H3zm2 2v.5l7 4.5 7-4.5V7zm0 2.8V17h14V9.8l-7 4.5z"/></svg>
        <span>john@northpeakdisposal.com</span>
      </div>
    </div>
    <div class="front-band">
      <span class="website">www.northpeakdisposal.com</span>
    </div>
  </section>

  <section class="card card-back">
    <div class="back-brand">
      <span class="brand-square"></span>
      <span class="brand-name">Northpeak<br>Clinical Disposal</span>
    </div>
  </section>
</main>
</body>
</html>
```